Hang Tags for New Dog Products

Hi,

I need a design put together for hangtags. The design would be for the front of a folded hangtag, which will be used for dog products.

The dog products are designed with vibrant colours, and are inspired by the outdoors and snow sports. The hang tags would also need to reflect this.

There are three different types of dog products, and if possible I would need three hangtags, same design but with the different product names.

Please find attached a sketch that I have made to give you an idea of an image I though would look ok. The hangtag will incorporate my logo, and underneath the product name.

Notes:

• My logo (attached) consists of the mountain, wolf and RB Pawz. This image and writing would have to stay the same, but can the colour be made more ice or neon blue to stand out.
• The three product names are Drift-Line Harness, Frost Ridge Collar and Bramble Lead
• With the bottom part of the hangtag I was thinking of making it half ice or neon blue with the writings colour changing on the blue, like image “sketch” attached. The two colours don’t have to be split down the middle, like the sketch,
• With the writing for Drift-Line Harness, Frost Ridge Collar and Bramble Lead. I am not going with a specific writing style, I will let the designer be creative on this. The writing in the “sketch” is just an example of how I would like it to cross colours from the white to the blue.
• I have also attached my logo separately. Like I mentioned before, the logo would have to stay the same, but if the colour was made more neon or ice blue that would be great.

Target Market(s)

Dog Owners

Colors
33a6d7
0393ce
85cae6

Requirements
Must have
• Full Logo
Nice to have
• Could the Logo's colour be changed to a more ice or neon blue to stand out.

```html
<!DOCTYPE html>
<html lang="en">
<head>
<meta charset="utf-8">
<title>RB Pawz Hang Tags</title>
<link href="https://fonts.googleapis.com/css2?family=Playfair+Display:wght@900&display=swap" rel="stylesheet">
<style>
  :root {
    --stage-light: #f4f4f4;
    --stage-dark: #d9d9d9;
    --tag-white: #ffffff;
    --pattern-tint: #eaf5fc;
    --brand-blue: #1f9fe0;
    --band-ice: #93d4f3;
    --hole-line: #222222;
  }
  html, body {
    margin: 0;
    padding: 0;
    overflow: hidden;
  }
  .canvas {
    position: relative;
    width: 1200px;
    height: 827px;
    overflow: hidden;
    background: radial-gradient(ellipse at center, var(--stage-light) 0%, var(--stage-dark) 100%);
  }
  .hang-tag {
    position: absolute;
    top: 68px;
    width: 462px;
    height: 690px;
    background: var(--tag-white);
    box-shadow: 0 1px 4px rgba(0, 0, 0, 0.12);
  }
  .hang-tag--harness { left: 86px; }
  .hang-tag--collar { left: 652px; }
  .hang-tag svg {
    display: block;
    width: 462px;
    height: 690px;
  }
  .brand-name,
  .product-name {
    font-family: "Playfair Display", Georgia, serif;
    font-weight: 900;
  }
  .brand-name {
    fill: var(--brand-blue);
    font-size: 84px;
  }
  .product-name {
    font-size: 70px;
  }
  .product-name--on-white { fill: var(--brand-blue); }
  .product-name--on-band {
    fill: var(--tag-white);
    stroke: var(--brand-blue);
    stroke-width: 1.4px;
    paint-order: stroke;
  }
</style>
</head>
<body>
<main class="canvas">

  <article class="hang-tag hang-tag--harness">
    <svg viewBox="0 0 462 690" xmlns="http://www.w3.org/2000/svg">
      <defs>
        <linearGradient id="pattern-tone-harness" x1="0" y1="0" x2="0" y2="1">
          <stop offset="0" stop-color="#eaf5fc"/>
          <stop offset="1" stop-color="#f6fbfe"/>
        </linearGradient>
        <clipPath id="band-clip-harness">
          <polygon points="226,444 462,444 462,690 230,690 230,540 242,530 230,520 244,508 230,496 244,484 230,470 242,458"/>
        </clipPath>
      </defs>
      <rect class="doodle-pattern" x="0" y="0" width="462" height="690" fill="url(#pattern-tone-harness)" role="img" aria-label="Faint hand-drawn pattern of dog toys, bones, bowls, paw prints and treats"/>
      <circle class="string-hole" cx="234" cy="42" r="8" fill="var(--tag-white)" stroke="var(--hole-line)" stroke-width="1"/>
      <text class="brand-name" x="231" y="300" text-anchor="middle">RB Pawz</text>
      <polygon class="colour-band" points="226,444 462,444 462,690 230,690 230,540 242,530 230,520 244,508 230,496 244,484 230,470 242,458" fill="var(--band-ice)"/>
      <g class="product-name product-name--on-white" text-anchor="middle">
        <text x="235" y="552" textLength="330" lengthAdjust="spacingAndGlyphs">DRIFT-LINE</text>
        <text x="235" y="620" textLength="300" lengthAdjust="spacingAndGlyphs">HARNESS</text>
      </g>
      <g class="product-name product-name--on-band" text-anchor="middle" clip-path="url(#band-clip-harness)">
        <text x="235" y="552" textLength="330" lengthAdjust="spacingAndGlyphs">DRIFT-LINE</text>
        <text x="235" y="620" textLength="300" lengthAdjust="spacingAndGlyphs">HARNESS</text>
      </g>
    </svg>
  </article>

  <article class="hang-tag hang-tag--collar">
    <svg viewBox="0 0 462 690" xmlns="http://www.w3.org/2000/svg">
      <defs>
        <linearGradient id="pattern-tone-collar" x1="0" y1="0" x2="0" y2="1">
          <stop offset="0" stop-color="#eaf5fc"/>
          <stop offset="1" stop-color="#f6fbfe"/>
        </linearGradient>
        <clipPath id="band-clip-collar">
          <polygon points="226,444 462,444 462,690 230,690 230,540 242,530 230,520 244,508 230,496 244,484 230,470 242,458"/>
        </clipPath>
      </defs>
      <rect class="doodle-pattern" x="0" y="0" width="462" height="690" fill="url(#pattern-tone-collar)" role="img" aria-label="Faint hand-drawn pattern of dog toys, bones, bowls, paw prints and treats"/>
      <circle class="string-hole" cx="234" cy="42" r="8" fill="var(--tag-white)" stroke="var(--hole-line)" stroke-width="1"/>
      <text class="brand-name" x="231" y="300" text-anchor="middle">RB Pawz</text>
      <polygon class="colour-band" points="226,444 462,444 462,690 230,690 230,540 242,530 230,520 244,508 230,496 244,484 230,470 242,458" fill="var(--band-ice)"/>
      <g class="product-name product-name--on-white" text-anchor="middle">
        <text x="235" y="552" textLength="330" lengthAdjust="spacingAndGlyphs">FROST RIDGE</text>
        <text x="235" y="620" textLength="250" lengthAdjust="spacingAndGlyphs">COLLAR</text>
      </g>
      <g class="product-name product-name--on-band" text-anchor="middle" clip-path="url(#band-clip-collar)">
        <text x="235" y="552" textLength="330" lengthAdjust="spacingAndGlyphs">FROST RIDGE</text>
        <text x="235" y="620" textLength="250" lengthAdjust="spacingAndGlyphs">COLLAR</text>
      </g>
    </svg>
  </article>

</main>
</body>
</html>
```